trading data display webpage

We have build a rough wireframe of the two webpages that we want to display .The two wireframes are attached as a pdf document.
there will be login page. after login , the user will see the index page. that is the first page of the wireframe.

what we are displaying is essentially spread data. we are taking the difference in prices are two places and displaying the data. some calculations are done and is shown in the grid.

below the grid we show the behaviour on a graph. we will use bubble chart. I did not find a sample, hence have thrown in a placeholder.

this is time series data ( changes daily) and hence we need to check the behaviour.

the second wire frame shows how the user will choose the source price points and the destination price points.
we are talking here of natural gas prices hence the reference to source prices and destination prices.

you need to design the page/ pages such that the end-user loves it and is easy to use. the intent here is easy to use and easy to understand.
this will be responsive webpage since the end user will check it out on a tablet or a smartphone.

so if possible tell us how the navigation bar, the button bar, etc should fall when the screen size decreases.

I have uploaded 2 files. one is the wireframe ( pdf document) and second is the logo file.

please also let us know where to place the logo.

Target Market(s)

the target market is traders and data analyst

Industry/Entity Type

Build

Colors

Designer to choose colors to be used in the design.

Requirements
Must have
• 1. design for the web.
2. but think how the design will look when the screen size decreases.
3. tell if possible what screen components to keep and what to hide.

```html
<!DOCTYPE html>
<html lang="en">
<head>
<meta charset="utf-8">
<title>Weekly Trading Stats</title>
<link rel="stylesheet" href="https://fonts.googleapis.com/css2?family=Open+Sans:wght@400;600;700&family=Oswald:wght@300;400&display=swap">
<style>
:root{
  --topbar:#222222;
  --teal:#16a085;
  --teal-dark:#138a72;
  --teal-tile:#19a88b;
  --page-bg:#e9e9e9;
  --panel:#ffffff;
  --border:#d9d9d9;
  --head-bg:#f2f2f2;
  --text:#333333;
  --muted:#888888;
  --green:#5cb85c;
  --red:#e74c3c;
  --blue:#3f88c9;
  --black:#333333;
  --slate:#6283a3;
}
*{box-sizing:border-box;margin:0;padding:0}
html,body{width:1200px;height:998px;overflow:hidden}
body{position:relative;background:var(--page-bg);font-family:"Open Sans",Arial,sans-serif;color:var(--text);font-size:13px}
.topbar{position:absolute;left:0;top:0;width:1200px;height:60px;background:var(--topbar);color:#fff}
.brand{position:absolute;left:22px;top:14px;display:flex;align-items:center;gap:14px;font-weight:700;font-size:18px}
.brand-dot{width:34px;height:34px;border-radius:50%;background:var(--teal)}
.alerts{position:absolute;left:850px;top:18px}
.icon-bell,.icon-warn{position:absolute;top:4px}
.icon-bell{left:0}
.icon-warn{left:40px}
.badge-count{position:absolute;left:12px;top:-9px;width:20px;height:20px;border:2px solid var(--red);border-radius:50%;background:var(--topbar);font-size:9px;font-weight:700;text-align:center;line-height:16px}
.top-links{position:absolute;left:952px;top:22px;display:flex;gap:31px;font-size:13px}
.avatar{position:absolute;left:1111px;top:15px;width:30px;height:30px;background:linear-gradient(135deg,#6b6b6b,#2e2e2e);border:1px solid #999}
.caret{position:absolute;left:1152px;top:28px}
.band{position:absolute;left:0;top:60px;width:1200px;height:153px;background:var(--teal)}
.nav{position:absolute;left:36px;top:71px;display:flex;gap:10px}
.nav-tile{width:100px;height:80px;border:1px solid rgba(0,0,0,.08);border-radius:3px;background:var(--teal-tile);color:#fff;font-size:14px;text-align:center;position:relative}
.nav-tile svg{display:block;margin:14px auto 8px}
.nav-tile.active{background:var(--teal-dark)}
.nav-tile.active:after{content:"";position:absolute;left:40px;bottom:-9px;border:9px solid transparent;border-bottom:0;border-top-color:var(--teal-dark)}
.main{position:absolute;left:36px;top:169px;width:1139px;height:829px;background:var(--panel);border-radius:4px 4px 0 0}
.stats-head{position:absolute;left:10px;top:11px;width:1119px;height:95px;background:linear-gradient(#ececec,#fff);border-radius:3px}
.page-title{position:absolute;left:15px;top:18px;font-family:"Oswald",sans-serif;font-size:19px;font-weight:400;color:#333}
.page-sub{position:absolute;left:173px;top:24px;font-family:"Oswald",sans-serif;font-weight:300;font-size:13px;color:#888}
.range{position:absolute;left:376px;top:20px;display:flex;border:1px solid #ccc;border-radius:3px;background:#fff;overflow:hidden}
.range span{padding:6px 10px;font-size:12px;border-left:1px solid #ccc}
.range span:first-child{border-left:0}
.range .on{background:#e3e3e3;box-shadow:inset 0 2px 4px rgba(0,0,0,.12)}
.stat{position:absolute;top:77px;width:250px;height:99px;background:#fff;border:1px solid var(--border);border-radius:3px;box-shadow:0 3px 0 -1px #f1f1f1,0 3px 0 0 #ddd}
.stat-label{position:absolute;left:13px;top:20px;font-size:10px;color:#888;letter-spacing:.3px}
.stat-value{position:absolute;left:13px;top:40px;font-family:"Oswald",sans-serif;font-size:26px;color:#333}
.pill{position:absolute;top:50px;padding:3px 7px;font-size:11px;font-weight:700;color:#fff;border-radius:2px}
.up{background:var(--green)}.down{background:var(--red)}
.panel{position:absolute;background:#fff;border:1px solid var(--border);border-radius:3px;overflow:hidden}
.panel-head{height:40px;background:var(--head-bg);border-bottom:1px solid var(--border);position:relative}
.panel-title{position:absolute;left:41px;top:9px;font-family:"Oswald",sans-serif;font-size:16px;font-weight:300;color:#333}
.panel-icon{position:absolute;left:14px;top:13px}
.trading{left:25px;top:193px;width:1091px;height:251px}
.trading .panel-head{height:58px}
.trading .panel-title{left:33px;top:17px}
.trading .panel-icon{left:5px;top:22px}
.select{position:absolute;top:11px;width:250px;height:34px;border:1px solid #ccc;border-radius:3px;background:#fff;font-weight:600;font-size:14px;padding:7px 9px}
.select:after{content:"";position:absolute;right:10px;top:14px;border:4px solid transparent;border-top:5px solid #777;border-bottom:0}
.cog-btn{position:absolute;right:6px;top:11px;width:44px;height:29px;border:1px solid #ccc;border-radius:3px;background:#fff}
table{width:100%;border-collapse:collapse}
th,td{border-right:1px solid #ddd;border-bottom:1px solid #ddd;text-align:left;padding:0 8px}
th:last-child,td:last-child{border-right:0;text-align:center}
th{height:36px;font-size:12px;font-weight:700;background:#f5f5f5}
td{height:39px;font-size:14px}
tbody tr:nth-child(odd) td{background:#f9f9f9}
tbody tr:last-child td{border-bottom:0}
.approve{display:inline-block;width:24px;height:22px;border-radius:3px;background:var(--red);vertical-align:middle}
.approve svg{display:block;margin:5px auto}
.pie-panel{left:25px;top:459px;width:529px;height:352px}
.bar-panel{left:586px;top:460px;width:530px;height:352px}
.chart{position:absolute;left:0;top:0}
.legend{position:absolute;font-size:11px;color:#333;line-height:17.5px}
.legend div{display:flex;align-items:center;gap:3px}
.legend i{display:inline-block;width:11px;height:11px;border:1px solid #fff;outline:1px solid #ccc}
</style>
</head>
<body>
<header class="topbar">
  <div class="brand"><span class="brand-dot"></span><span>Company Name here</span></div>
  <div class="alerts">
    <svg class="icon-bell" width="20" height="20" viewBox="0 0 20 20"><path d="M10 1c-3.3 0-5.5 2.5-5.5 6v4L2.5 15h15l-2-4V7C15.5 3.5 13.3 1 10 1zM7.5 16.5a2.5 2.5 0 005 0z" fill="#444"/></svg>
    <span class="badge-count">3</span>
    <svg class="icon-warn" width="22" height="20" viewBox="0 0 22 20"><path d="M11 1L1 19h20z" fill="#555"/><rect x="10" y="7" width="2" height="6" fill="#222"/><rect x="10" y="15" width="2" height="2" fill="#222"/></svg>
  </div>
  <nav class="top-links"><span>About</span><span>Resources</span></nav>
  <div class="avatar" role="img" aria-label="User profile photo"></div>
  <svg class="caret" width="10" height="6" viewBox="0 0 10 6"><path d="M0 0h10L5 6z" fill="#fff"/></svg>
</header>

<div class="band"></div>
<nav class="nav">
  <div class="nav-tile active"><svg width="22" height="22" viewBox="0 0 22 22"><rect x="1" y="1" width="20" height="20" rx="3" fill="#fff"/><rect x="4" y="4" width="14" height="14" fill="#138a72"/><path d="M14 6v10L7 11z" fill="#fff"/></svg>West</div>
  <div class="nav-tile"><svg width="22" height="22" viewBox="0 0 22 22"><circle cx="11" cy="11" r="9" fill="none" stroke="#fff" stroke-width="3"/><path d="M15 7l-2 6-6 2 2-6z" fill="#fff"/></svg>Central</div>
  <div class="nav-tile"><svg width="22" height="22" viewBox="0 0 22 22"><rect x="1" y="1" width="20" height="20" rx="3" fill="#fff"/><rect x="4" y="4" width="14" height="14" fill="#19a88b"/><path d="M8 6v10l7-5z" fill="#fff"/></svg>East</div>
  <div class="nav-tile"><svg width="24" height="24" viewBox="0 0 24 24"><g fill="#fff"><circle cx="12" cy="12" r="7.5"/><rect x="10" y="1" width="4" height="22" rx="1"/><rect x="1" y="10" width="22" height="4" rx="1"/><rect x="10" y="1" width="4" height="22" rx="1" transform="rotate(45 12 12)"/><rect x="10" y="1" width="4" height="22" rx="1" transform="rotate(-45 12 12)"/></g><circle cx="12" cy="12" r="3.5" fill="#19a88b"/></svg>Settings</div>
  <div class="nav-tile"><svg width="24" height="22" viewBox="0 0 24 22"><path d="M9 2H4a3 3 0 00-3 3v12a3 3 0 003 3h5v-3H4V5h5z" fill="#fff"/><path d="M8 8h7V4l8 7-8 7v-4H8z" fill="#fff"/></svg>Logout</div>
</nav>

<main class="main">
  <section class="stats-head">
    <h1 class="page-title">Weekly Trading Stats</h1>
    <span class="page-sub">For the week of Jun 02 - Jun 09, 2014</span>
    <div class="range"><span>5 Days</span><span class="on">7 Days</span><span>18 Days</span><span>Month</span><span>Year</span></div>
  </section>

  <div class="stat" style="left:25px"><div class="stat-label">TOTAL NET PROFIT</div><div class="stat-value">$4097.00</div><span class="pill up" style="left:114px">+43%</span></div>
  <div class="stat" style="left:305px"><div class="stat-label">GROSS PROFIT</div><div class="stat-value">$4150.50</div><span class="pill up" style="left:112px">+37%</span></div>
  <div class="stat" style="left:585px"><div class="stat-label">AVERAGE TRADE</div><div class="stat-value">$75.88</div><span class="pill up" style="left:88px">+26%</span></div>
  <div class="stat" style="left:865px"><div class="stat-label">MAXIMUM DRAWDOWN</div><div class="stat-value">37.50</div><span class="pill down" style="left:73px">-5%</span></div>

  <section class="panel trading">
    <div class="panel-head">
      <svg class="panel-icon" width="16" height="13" viewBox="0 0 16 13"><g fill="#666"><rect x="0" y="0" width="3" height="2"/><rect x="4" y="0" width="12" height="2"/><rect x="0" y="4" width="3" height="2"/><rect x="4" y="4" width="12" height="2"/><rect x="0" y="8" width="3" height="2"/><rect x="4" y="8" width="12" height="2"/></g></svg>
      <h2 class="panel-title">Trading Data</h2>
      <div class="select" style="left:155px">Select Source Indice</div>
      <div class="select" style="left:442px">Select Destination Indice</div>
      <div class="cog-btn"><svg width="44" height="29" viewBox="0 0 44 29"><circle cx="17" cy="14" r="4" fill="none" stroke="#333" stroke-width="3" stroke-dasharray="2 1.2"/><circle cx="17" cy="14" r="2.5" fill="#333"/><path d="M25 13h6l-3 3z" fill="#333"/></svg></div>
    </div>
    <table>
      <thead><tr>
        <th style="width:165px">Spread-name</th><th style="width:117px">avg sprd</th><th style="width:118px">+ve Prob</th><th style="width:114px">-ve Prob</th><th style="width:138px">Spike Prob</th><th style="width:141px">Avg Supply</th><th style="width:205px">Supply cut-probe</th><th>Approved</th>
      </tr></thead>
      <tbody>
        <tr><td>Spread 1</td><td>item 1</td><td></td><td></td><td></td><td></td><td></td><td><span class="approve"><svg width="12" height="11" viewBox="0 0 12 11"><path d="M1 6l3.5 3.5L11 2" fill="none" stroke="#fff" stroke-width="2.4"/></svg></span></td></tr>
        <tr><td>Spread 2</td><td>item 2</td><td></td><td></td><td></td><td></td><td></td><td><span class="approve"><svg width="12" height="11" viewBox="0 0 12 11"><path d="M1 6l3.5 3.5L11 2" fill="none" stroke="#fff" stroke-width="2.4"/></svg></span></td></tr>
        <tr><td>Spread 3</td><td>item 3</td><td></td><td></td><td></td><td></td><td></td><td><span class="approve"><svg width="12" height="11" viewBox="0 0 12 11"><path d="M1 6l3.5 3.5L11 2" fill="none" stroke="#fff" stroke-width="2.4"/></svg></span></td></tr>
        <tr><td>Spread 4</td><td>item 4</td><td></td><td></td><td></td><td></td><td></td><td><span class="approve"><svg width="12" height="11" viewBox="0 0 12 11"><path d="M1 6l3.5 3.5L11 2" fill="none" stroke="#fff" stroke-width="2.4"/></svg></span></td></tr>
      </tbody>
    </table>
  </section>

  <section class="panel pie-panel">
    <div class="panel-head">
      <svg class="panel-icon" width="16" height="14" viewBox="0 0 16 14"><rect x="0.5" y="0.5" width="15" height="13" fill="none" stroke="#777"/><g fill="#777"><rect x="3" y="7" width="2" height="5"/><rect x="6" y="4" width="2" height="8"/><rect x="9" y="6" width="2" height="6"/><rect x="12" y="3" width="2" height="9"/></g></svg>
      <h2 class="panel-title">Spread vs Supply</h2>
    </div>
    <svg class="chart" width="529" height="352" viewBox="61 628 529 352" aria-label="Pie chart of spread versus supply">
      <g stroke="#fff" stroke-width="4" stroke-linejoin="round">
        <path d="M294 822L294 686A136 136 0 0 1 419.2 768.9Z" fill="#16a085"/>
        <path d="M294 822L419.2 768.9A136 136 0 0 1 373.9 932Z" fill="#e74c3c"/>
        <path d="M294 822L373.9 932A136 136 0 0 1 162.6 786.8Z" fill="#3f88c9"/>
        <path d="M294 822L162.6 786.8A136 136 0 0 1 185.4 740.2Z" fill="#333"/>
        <path d="M294 822L185.4 740.2A136 136 0 0 1 294 686Z" fill="#6283a3"/>
      </g>
      <circle cx="294" cy="822" r="70" fill="none" stroke="#fff" stroke-width="1"/>
    </svg>
    <div class="legend" style="left:445px;top:61px">
      <div><i style="background:var(--teal)"></i>Product 1</div>
      <div><i style="background:var(--red)"></i>Product 2</div>
      <div><i style="background:var(--blue)"></i>Product 3</div>
      <div><i style="background:var(--black)"></i>Product 4</div>
      <div><i style="background:var(--slate)"></i>Product 5</div>
    </div>
  </section>

  <section class="panel bar-panel">
    <div class="panel-head">
      <svg class="panel-icon" width="16" height="14" viewBox="0 0 16 14"><rect x="0.5" y="0.5" width="15" height="13" fill="none" stroke="#777"/><g fill="#777"><rect x="3" y="7" width="2" height="5"/><rect x="6" y="4" width="2" height="8"/><rect x="9" y="6" width="2" height="6"/><rect x="12" y="3" width="2" height="9"/></g></svg>
      <h2 class="panel-title">Spreads Across Time</h2>
    </div>
    <svg class="chart" width="530" height="352" viewBox="622 629 530 352" aria-label="Stacked bar chart of spreads from January to May" font-family="Open Sans, sans-serif" font-size="11" fill="#555">
      <g stroke="#ddd" stroke-width="1">
        <line x1="666" y1="690.5" x2="1132" y2="690.5"/><line x1="666" y1="731.5" x2="1132" y2="731.5"/><line x1="666" y1="773.5" x2="1132" y2="773.5"/><line x1="666" y1="814.5" x2="1132" y2="814.5"/><line x1="666" y1="855.5" x2="1132" y2="855.5"/><line x1="666" y1="897.5" x2="1132" y2="897.5"/><line x1="666" y1="938.5" x2="1132" y2="938.5" stroke="#bbb"/>
      </g>
      <g text-anchor="end">
        <text x="662" y="694">3000</text><text x="662" y="735">2500</text><text x="662" y="777">2000</text><text x="662" y="818">1500</text><text x="662" y="859">1000</text><text x="662" y="901">500</text><text x="662" y="942">0</text>
      </g>
      <g text-anchor="middle"><text x="718" y="956">Jan</text><text x="898" y="956">Mar</text><text x="1081" y="956">May</text></g>
      <g>
        <rect x="703" y="839" width="33" height="99" fill="#16a085"/><rect x="703" y="773" width="33" height="66" fill="#e74c3c"/><rect x="703" y="719" width="33" height="54" fill="#3f88c9"/>
        <rect x="796" y="881" width="33" height="57" fill="#16a085"/><rect x="796" y="831" width="33" height="50" fill="#e74c3c"/><rect x="796" y="794" width="33" height="37" fill="#3f88c9"/>
        <rect x="882" y="856" width="33" height="82" fill="#16a085"/><rect x="882" y="831" width="33" height="25" fill="#e74c3c"/><rect x="882" y="819" width="33" height="12" fill="#3f88c9"/>
        <rect x="975" y="889" width="33" height="49" fill="#16a085"/><rect x="975" y="860" width="33" height="29" fill="#e74c3c"/><rect x="975" y="844" width="33" height="16" fill="#3f88c9"/>
        <rect x="1065" y="909" width="33" height="29" fill="#16a085"/><rect x="1065" y="885" width="33" height="24" fill="#e74c3c"/><rect x="1065" y="872" width="33" height="13" fill="#3f88c9"/>
      </g>
    </svg>
    <div class="legend" style="left:443px;top:66px">
      <div><i style="background:var(--teal)"></i>Product 1</div>
      <div><i style="background:var(--red)"></i>Product 2</div>
      <div><i style="background:var(--blue)"></i>Product 3</div>
    </div>
  </section>
</main>
</body>
</html>
```